New VPN Company needs a Web Site

This competition is the first step of a 3 step project.
- Step 1: (This project) We are looking to have 3 pages designed to evaluate your design and illustration skills.
- Step 2: Once we find a winner, we will request a bid to have the rest of the website designed.
- Step 3: We will request a bid to have the designs converted into WordPress if the bid is acceptable.
If you have the capabilities, Steps 2 and 3 can be combined into a single project/bid.
Design Notes
- Design type should be “FLAT.”
- Clean, crisp design that communicates security, anonymity, encryption, privacy.
- Please take a look at the following website: http://brisk.tallowvpn.com This is our current Word Press based setup. It contains all the link structures, menus, and text for the website. PLEASE NOTE THAT THE CURRENT DESIGN HAS NOTHING TO DO WITH WHAT YOU ARE DESIGNING. I USED THE FIRST WORD PRESS TEMPLATE THAT I COULD FIND. Once you submit a winning design, either YOU (if you have the skill set) or somebody else will take the designs and convert it into a word press template.
Here are a few of the pages from http://brisk.tallowvpn.com that I would like to see mockups for:
o Main Page: http://brisk.tallowvpn.com
Notes
• I have a dummy graphic up. That graphic needs to be replaced. Also as per the “Should have’s” I want all pages to have unlimited stretching right and left without that grey border on the right and left sides that are currently present.)
o Features Page: http://brisk.tallowvpn.com/index.php/features/
o Windows App download Page: http://brisk.tallowvpn.com/index.php/vpn-apps/vpn-for-windows/

- I want a “top bar” which shows Your IP: Your ISP: Your Location: Your Status: Like most of my competitors have.
- This website needs several original illustrations.
- The website must be clean, uncluttered, and concise.
- Use the copy provided from the http://brisk.tallowvpn.com website.
- Colors are up to the designers; this includes logo colors

- Please take a look at some of our competitor's websites for overall inspiration:
o https://www.quarrylantern.com
o https://plumvpn.com
o https://www.fernwickbay.com/en-us/index
o https://www.tidalvpn.com/
o https://www.oakvpn.com/
o https://www.netmoraly.com/
o https://www.lumbrafoxvpn.com/en_US/

Target Market(s)

Consumers between 18-30 from around the world.

Industry/Entity Type

Internet Service Provider

Number of Pages Required

3 page

Colors

Designer to choose colors to be used in the design.

Requirements
Must have
• - Look great on Desktop, Tablet, and smartphones.
• - The current template has borders. I want the new design to stretch with the browser, e.g., no grey borders on the left and right of the screen.
• - All illustration work must be original. We are not interested in stock photos.
• - Use attached logo. Font is Nexa Xbold.
Should not have
• - A nonfunctional look on smartphones. A high percentage of purchases will be made by smartphone users.
• - Should only have solid colors (two tone or three tone is ok). I am not a big fan of gradients or soft shadows.

```html
<!DOCTYPE html>
<html lang="en">
<head>
<meta charset="utf-8">
<title>TallowVPN – Fast and Ultra Secure Offshore VPN</title>
<link href="https://fonts.googleapis.com/css2?family=Poppins:wght@400;500;600;700&family=Open+Sans:ital,wght@0,400;0,600;1,400&display=swap" rel="stylesheet">
<style>
:root{
  --red:#f2483c;
  --red-dark:#d93a2f;
  --ink:#1b1b1b;
  --text:#4a4a4a;
  --muted:#8a8a8a;
  --hero-bg:#ebebeb;
  --light-bg:#f3f3f3;
  --line:#dcdcdc;
  --card-dark:#2b2b2b;
  --footer-bg:#050505;
  --white:#ffffff;
}
*{box-sizing:border-box;margin:0;padding:0}
html,body{width:1200px;height:3629px;overflow:hidden}
body{font-family:"Open Sans",Arial,sans-serif;color:var(--text);background:var(--white);position:relative}
h1,h2,h3,h4,.heading{font-family:"Poppins",Arial,sans-serif;color:var(--ink)}
a{color:inherit;text-decoration:none}
.abs{position:absolute}
section,header,footer,.status-bar{position:relative;width:1200px}

/* status bar */
.status-bar{height:29px;background:var(--white);display:flex;justify-content:center;align-items:center;gap:46px;font-size:12px;color:#333}
.status-bar .warn{color:var(--red)}

/* hero */
.hero{height:636px;background:var(--hero-bg)}
.brand{display:flex;align-items:center;gap:10px;font-family:"Poppins",Arial,sans-serif;font-weight:700;color:var(--red);font-size:30px;letter-spacing:.5px}
.brand-dot{width:44px;height:44px;border-radius:50%;background:var(--red)}
.hero .brand{left:176px;top:40px}
.main-nav{left:588px;top:48px;display:flex;gap:34px;font-family:"Poppins",Arial,sans-serif;font-weight:600;font-size:15px;color:var(--ink)}
.hero-title{left:0;width:1200px;top:140px;text-align:center}
.hero-title h1{font-size:37px;font-weight:600;line-height:48px}
.hero-title h2{font-size:29px;font-weight:600;line-height:42px}
.btn{display:inline-flex;align-items:center;justify-content:center;gap:8px;border-radius:30px;font-family:"Poppins",Arial,sans-serif;font-weight:500}
.btn-solid{background:var(--red);color:var(--white)}
.btn-outline{border:2px solid var(--red);color:var(--red);background:var(--white)}
.btn-dark{background:var(--ink);color:var(--white)}
.hero .btn{left:501px;top:240px;width:198px;height:48px;font-size:17px}
.hero-art{left:0;top:298px;width:1200px;height:338px;background:linear-gradient(180deg,#e9e9e9 0%,#e4e4e4 55%,#f1c53a 55%,#f4cd45 66%,#f0f0f0 66%,#ececec 100%)}
.slider-arrow{width:30px;height:60px}
.hero .arrow-left{left:98px;top:310px}
.hero .arrow-right{left:1072px;top:310px}

/* partners */
.partners{height:90px;border-bottom:2px solid var(--line);display:flex;justify-content:center;align-items:center;gap:76px}
.partner-mark{width:110px;height:30px;background:#c9c9c9;border-radius:4px}

/* about */
.about{height:453px}
.about-art{left:121px;top:45px;width:448px;height:312px;border-radius:8px;background:linear-gradient(135deg,#fde3df 0%,#f7a69e 55%,#f2483c 100%)}
.about h2{left:593px;top:84px;font-size:38px;font-weight:700}
.about h2 span{color:var(--red)}
.about .copy{left:593px;top:150px;width:470px;font-size:14px;line-height:24px;color:var(--muted)}
.about .copy p+p{margin-top:14px}
.about .btn{left:590px;top:340px;width:152px;height:40px;font-size:13px}

/* guarantee band */
.guarantee{height:223px;background:var(--red);text-align:center;color:var(--white)}
.badge-circle{width:56px;height:56px;border-radius:50%;background:var(--red);border:5px solid var(--white);left:572px;top:-28px}
.guarantee h2{position:absolute;top:46px;width:100%;color:var(--white);font-size:29px;font-weight:600}
.guarantee p{position:absolute;top:96px;width:100%;font-size:19px}
.guarantee .btn{left:498px;top:138px;width:204px;height:50px;font-size:17px}

/* features */
.features{height:552px}
.section-title{width:100%;text-align:center;font-size:36px;font-weight:600}
.section-title span{color:var(--red)}
.features .section-title{position:absolute;top:60px}
.feature-card{top:140px;width:256px;height:346px;border:2px solid #cfcfcf;border-radius:120px 120px 70px 70px;text-align:center;background:var(--white)}
.feature-card svg{position:absolute;left:93px;top:40px}
.feature-card h3{position:absolute;top:124px;width:100%;font-size:15px;font-weight:600;line-height:20px;padding:0 26px}
.feature-card p{position:absolute;top:172px;width:100%;padding:0 30px;font-size:12.5px;line-height:19px;color:var(--muted)}
.feature-card .btn{left:56px;top:275px;width:140px;height:36px;font-size:12px}
.round-arrow{width:46px;height:46px;border-radius:50%;top:282px}
.round-arrow.light{background:#c9c9c9;left:91px}
.round-arrow.dark{background:#333;left:1054px}

/* pricing */
.pricing{height:878px;background:var(--light-bg)}
.pricing .section-title{position:absolute;top:44px}
.price-panel{left:182px;top:145px;width:847px;height:295px;background:var(--white);border:1px solid var(--line)}
.plan{top:0;width:282px;height:295px;text-align:center}
.plan h4{position:absolute;top:38px;width:100%;font-size:15px;font-weight:600}
.plan .price{position:absolute;top:70px;width:100%;font-family:"Poppins",Arial,sans-serif;font-size:38px;font-weight:600;color:var(--ink)}
.plan .price sup{font-size:20px;vertical-align:18px}
.plan .per{position:absolute;top:122px;width:100%;font-size:10px;color:var(--muted);letter-spacing:.5px}
.plan .save{position:absolute;top:150px;left:50%;transform:translateX(-50%);padding:3px 16px;border-radius:14px;background:#e3e3e3;font-size:13px;color:#333}
.plan .note{position:absolute;top:180px;width:100%;font-size:13px;color:#555}
.plan .btn{position:absolute;left:48px;top:230px;width:186px;height:42px;font-size:15px}
.plan-featured{left:450px;top:2115px;width:300px;height:325px;background:var(--card-dark);text-align:center;position:absolute}
.plan-featured h4,.plan-featured .price{color:var(--white)}
.plan-featured h4{top:40px}
.plan-featured .price{top:72px}
.plan-featured .per{top:124px;color:#bbb}
.plan-featured .save{top:152px;background:#111;color:var(--white)}
.plan-featured .note{top:182px;color:#ccc}
.plan-featured .btn{left:34px;top:252px;width:232px;height:44px}
.perks{top:525px;width:440px;list-style:none}
.perks li{display:flex;align-items:center;gap:12px;height:32.6px;font-size:13px;color:#333}
.perks svg{flex:none}

/* testimonials */
.testimonials{height:421px}
.testimonials .section-title{position:absolute;top:62px;font-size:32px}
.portrait{left:230px;top:133px;width:170px;height:170px;border-radius:50%;background:radial-gradient(circle at 50% 40%,#d9b8a0 0%,#c29b80 45%,#e8e8e8 72%)}
.quote-mark{left:362px;top:229px;width:50px;height:50px;border-radius:50%;background:var(--red);color:var(--white);font-family:"Poppins",Arial,sans-serif;font-size:40px;font-weight:700;text-align:center;line-height:62px}
.testimonial-rule{left:452px;top:150px;width:2px;height:120px;background:var(--line)}
.testimonial-text{left:468px;top:140px;width:520px;font-style:italic;font-size:17px;line-height:32px;color:var(--muted)}
.testimonial-author{left:468px;top:250px;font-size:14px;font-weight:600;color:#333;letter-spacing:.5px}
.dots{left:476px;top:296px;display:flex;gap:6px}
.dots span{width:7px;height:7px;border-radius:50%;background:#333}
.dots span:first-child{background:#9a9a9a}
.testimonials .arrow-left{left:130px;top:196px}
.testimonials .arrow-right{left:1028px;top:196px}

/* footer */
.site-footer{height:345px;background:var(--footer-bg);color:#bdbdbd}
.footer-brand{left:180px;top:80px;flex-direction:column;gap:12px;font-size:26px}
.footer-brand .brand-dot{width:70px;height:70px}
.footer-col{top:70px}
.footer-col h4{color:var(--white);font-size:15px;font-weight:600;letter-spacing:.5px;margin-bottom:16px}
.footer-col li{list-style:none;font-size:13px;line-height:24px}
.footer-bottom{left:186px;top:273px;width:840px;border-top:1px solid #2a2a2a}
.copyright{left:190px;top:298px;font-size:12px;color:#8a8a8a}
.social{left:858px;top:294px;display:flex;gap:26px}
.social span{width:14px;height:14px;border-radius:50%;background:#9a9a9a}
</style>
</head>
<body>

<div class="status-bar">
  <span>Your IP address: 103.44.54.96</span>
  <span>Your ISP:Tallow VPN Pvt. Ltd.</span>
  <span>Your Locaton: Chicago</span>
  <span class="warn">You are not protected.</span>
</div>

<header class="hero">
  <a class="brand abs" href="#"><span class="brand-dot"></span>TallowVPN</a>
  <nav class="main-nav abs">
    <a href="#">About</a><a href="#">Features</a><a href="#">VPN APPS</a><a href="#">Pricing</a><a href="#">Support</a>
  </nav>
  <div class="hero-title abs">
    <h1>Fast and Ultra Secure Offshore based</h1>
    <h2>VPN Solutionwith thousands of servers</h2>
  </div>
  <a class="btn btn-solid abs" href="#">Get Started <span>→</span></a>
  <div class="hero-art abs" role="img" aria-label="Illustration of a white desk with a yellow top holding a laptop showing a world map, a tablet and a phone with the padlock app, a pencil cup and a wooden figure, with a white chair in front"></div>
  <svg class="slider-arrow abs arrow-left" viewBox="0 0 30 60"><polyline points="26,4 4,30 26,56" fill="none" stroke="#555" stroke-width="2.5"/></svg>
  <svg class="slider-arrow abs arrow-right" viewBox="0 0 30 60"><polyline points="4,4 26,30 4,56" fill="none" stroke="#555" stroke-width="2.5"/></svg>
</header>

<section class="partners" aria-label="Partners">
  <span class="partner-mark"></span><span class="partner-mark"></span><span class="partner-mark"></span><span class="partner-mark"></span><span class="partner-mark"></span>
</section>

<section class="about">
  <div class="about-art abs" role="img" aria-label="Isometric illustration of a red server tower linked by circuit lines to laptops, phones and padlocks"></div>
  <h2 class="abs">About <span>TALLOW VPN</span></h2>
  <div class="copy abs">
    <p>Mauris vel lacus vitae felis vestibulum volutpat Etiam est nunc venenatis in tristique eu imperdiet ac nisl Cum</p>
    <p>sociis natoque penatibus et magnis dis parturient montes nascetur ridiculus mus In iaculis facilisis massa Etiam eu urna Sed porta Suspendisse quam leo molestie sed luctus quis feugiat in pede Fusce tellus Sed metus augue convallis et vehicula</p>
  </div>
  <a class="btn btn-solid abs" href="#">Read More →</a>
</section>

<section class="guarantee">
  <span class="badge-circle abs"></span>
  <h2>31 Day Unconditional Money Back Guarantee</h2>
  <p>Mauris vel lacus vitae felis vestibulum volutpat Etiam est nunc</p>
  <a class="btn btn-dark abs" href="#">Click here →</a>
</section>

<section class="features">
  <h2 class="section-title">Our <span>Features</span></h2>
  <span class="round-arrow light abs"><svg width="46" height="46" viewBox="0 0 46 46"><polyline points="26,15 18,23 26,31" fill="none" stroke="#333" stroke-width="3"/></svg></span>
  <span class="round-arrow dark abs"><svg width="46" height="46" viewBox="0 0 46 46"><polyline points="20,15 28,23 20,31" fill="none" stroke="#fff" stroke-width="3"/></svg></span>

  <article class="feature-card abs" style="left:182px">
    <svg width="70" height="70" viewBox="0 0 70 70" fill="none" stroke="#f2483c" stroke-width="2.5"><rect x="14" y="8" width="42" height="32" rx="2"/><rect x="6" y="40" width="58" height="8" rx="2"/><rect x="28" y="52" width="14" height="12"/><path d="M31 52v-4a4 4 0 0 1 8 0v4"/></svg>
    <h3>Military grade 256 bit encryption</h3>
    <p>Nobody can spy on your internet activities because we route it through securely encrypted tunnels.</p>
    <a class="btn btn-outline abs" href="#">Read More →</a>
  </article>

  <article class="feature-card abs" style="left:470px">
    <svg width="70" height="70" viewBox="0 0 70 70" fill="none" stroke="#f2483c" stroke-width="2.5"><path d="M35 6l24 9v18c0 15-10 25-24 31C21 58 11 48 11 33V15z"/><polyline points="24,34 32,42 47,25"/></svg>
    <h3>Absolute NO LOGGING Policy</h3>
    <p>We do not permanently log any of your online activities. This ensures total privacy and anonymity</p>
    <a class="btn btn-outline abs" href="#">Read More →</a>
  </article>

  <article class="feature-card abs" style="left:757px">
    <svg width="70" height="70" viewBox="0 0 70 70" fill="none" stroke="#f2483c" stroke-width="2.5"><rect x="6" y="10" width="58" height="38" rx="2"/><polygon points="29,20 44,29 29,38"/><line x1="24" y1="58" x2="46" y2="58"/><line x1="35" y1="48" x2="35" y2="58"/></svg>
    <h3>Watch Your Favorite Streaming Channels</h3>
    <p>Tallowvpn works flawlessly with your favorite streaming channels such as Streamly, Vidora etc. Your ISP might monitor</p>
    <a class="btn btn-outline abs" href="#">Read More →</a>
  </article>
</section>

<section class="pricing">
  <span class="badge-circle abs"></span>
  <h2 class="section-title">Our <span>Pricing</span></h2>

  <div class="price-panel abs">
    <div class="plan abs" style="left:0">
      <h4>MONTHLY</h4>
      <div class="price"><sup>$</sup>10.95</div>
      <div class="per">MONTHLY</div>
      <span class="save">NO SAVINGS</span>
      <div class="note">31 Day Money Back Guarantee</div>
      <a class="btn btn-outline" href="#">Get tallowVPN →</a>
    </div>
    <div class="plan abs" style="left:565px">
      <h4>YEARLY</h4>
      <div class="price"><sup>$</sup>5.41</div>
      <div class="per">MONTHLY</div>
      <span class="save">SAVE 51%</span>
      <div class="note">31 Day Money Back Guarantee</div>
      <a class="btn btn-outline" href="#">Get tallowVPN →</a>
    </div>
  </div>

  <ul class="perks abs" style="left:206px">
    <li><svg width="16" height="16" viewBox="0 0 16 16"><circle cx="8" cy="8" r="8" fill="#f2483c"/><polyline points="4.5,8.3 7,10.8 11.5,5.5" fill="none" stroke="#fff" stroke-width="2"/></svg>Apps for all of your favorite devices</li>
    <li><svg width="16" height="16" viewBox="0 0 16 16"><circle cx="8" cy="8" r="8" fill="#f2483c"/><polyline points="4.5,8.3 7,10.8 11.5,5.5" fill="none" stroke="#fff" stroke-width="2"/></svg>X000 IP addresses from across the globe</li>
    <li><svg width="16" height="16" viewBox="0 0 16 16"><circle cx="8" cy="8" r="8" fill="#f2483c"/><polyline points="4.5,8.3 7,10.8 11.5,5.5" fill="none" stroke="#fff" stroke-width="2"/></svg>256 bit AES encryption</li>
    <li><svg width="16" height="16" viewBox="0 0 16 16"><circle cx="8" cy="8" r="8" fill="#f2483c"/><polyline points="4.5,8.3 7,10.8 11.5,5.5" fill="none" stroke="#fff" stroke-width="2"/></svg>OpenVPN/IKEv2/L2TP/IPSec/PPTP/SSTP protocol support</li>
    <li><svg width="16" height="16" viewBox="0 0 16 16"><circle cx="8" cy="8" r="8" fill="#f2483c"/><polyline points="4.5,8.3 7,10.8 11.5,5.5" fill="none" stroke="#fff" stroke-width="2"/></svg>Strict NO-LOGGING policy</li>
    <li><svg width="16" height="16" viewBox="0 0 16 16"><circle cx="8" cy="8" r="8" fill="#f2483c"/><polyline points="4.5,8.3 7,10.8 11.5,5.5" fill="none" stroke="#fff" stroke-width="2"/></svg>P2P Friendly / Unlimited P2P traffic</li>
    <li><svg width="16" height="16" viewBox="0 0 16 16"><circle cx="8" cy="8" r="8" fill="#f2483c"/><polyline points="4.5,8.3 7,10.8 11.5,5.5" fill="none" stroke="#fff" stroke-width="2"/></svg>Unblock Streaming Services and watch Streamly/Vidora/Cinebox and more</li>
    <li><svg width="16" height="16" viewBox="0 0 16 16"><circle cx="8" cy="8" r="8" fill="#f2483c"/><polyline points="4.5,8.3 7,10.8 11.5,5.5" fill="none" stroke="#fff" stroke-width="2"/></svg>31 Day UNCONDITIONAL money back guarantee</li>
    <li><svg width="16" height="16" viewBox="0 0 16 16"><circle cx="8" cy="8" r="8" fill="#f2483c"/><polyline points="4.5,8.3 7,10.8 11.5,5.5" fill="none" stroke="#fff" stroke-width="2"/></svg>Use on up to X devices simultaneously</li>
    <li><svg width="16" height="16" viewBox="0 0 16 16"><circle cx="8" cy="8" r="8" fill="#f2483c"/><polyline points="4.5,8.3 7,10.8 11.5,5.5" fill="none" stroke="#fff" stroke-width="2"/></svg>Anonymous torrenting</li>
  </ul>
  <ul class="perks abs" style="left:668px">
    <li><svg width="16" height="16" viewBox="0 0 16 16"><circle cx="8" cy="8" r="8" fill="#f2483c"/><polyline points="4.5,8.3 7,10.8 11.5,5.5" fill="none" stroke="#fff" stroke-width="2"/></svg>SOCKS5 Web Proxy</li>
    <li><svg width="16" height="16" viewBox="0 0 16 16"><circle cx="8" cy="8" r="8" fill="#f2483c"/><polyline points="4.5,8.3 7,10.8 11.5,5.5" fill="none" stroke="#fff" stroke-width="2"/></svg>Unlimited server switching</li>
    <li><svg width="16" height="16" viewBox="0 0 16 16"><circle cx="8" cy="8" r="8" fill="#f2483c"/><polyline points="4.5,8.3 7,10.8 11.5,5.5" fill="none" stroke="#fff" stroke-width="2"/></svg>VPN tunneling available for extra security</li>
    <li><svg width="16" height="16" viewBox="0 0 16 16"><circle cx="8" cy="8" r="8" fill="#f2483c"/><polyline points="4.5,8.3 7,10.8 11.5,5.5" fill="none" stroke="#fff" stroke-width="2"/></svg>Incorporated Offshore</li>
    <li><svg width="16" height="16" viewBox="0 0 16 16"><circle cx="8" cy="8" r="8" fill="#f2483c"/><polyline points="4.5,8.3 7,10.8 11.5,5.5" fill="none" stroke="#fff" stroke-width="2"/></svg>IP leaking protection against IPV6 and DNS leaks</li>
    <li><svg width="16" height="16" viewBox="0 0 16 16"><circle cx="8" cy="8" r="8" fill="#f2483c"/><polyline points="4.5,8.3 7,10.8 11.5,5.5" fill="none" stroke="#fff" stroke-width="2"/></svg>Internet Kill Switch</li>
    <li><svg width="16" height="16" viewBox="0 0 16 16"><circle cx="8" cy="8" r="8" fill="#f2483c"/><polyline points="4.5,8.3 7,10.8 11.5,5.5" fill="none" stroke="#fff" stroke-width="2"/></svg>Unlimited Data Transfer</li>
    <li><svg width="16" height="16" viewBox="0 0 16 16"><circle cx="8" cy="8" r="8" fill="#f2483c"/><polyline points="4.5,8.3 7,10.8 11.5,5.5" fill="none" stroke="#fff" stroke-width="2"/></svg>X Servers in over X countries</li>
    <li><svg width="16" height="16" viewBox="0 0 16 16"><circle cx="8" cy="8" r="8" fill="#f2483c"/><polyline points="4.5,8.3 7,10.8 11.5,5.5" fill="none" stroke="#fff" stroke-width="2"/></svg>Use your favorite social networks anywhere</li>
  </ul>
</section>

<div class="plan plan-featured">
  <h4>TWO YEARS</h4>
  <div class="price"><sup>$</sup>3.51</div>
  <div class="per">MONTHLY</div>
  <span class="save">SAVE 68%</span>
  <div class="note">31 Day Money Back Guarantee</div>
  <a class="btn btn-solid" href="#">Get tallowVPN →</a>
</div>

<section class="testimonials">
  <h2 class="section-title">Testimonials</h2>
  <svg class="slider-arrow abs arrow-left" viewBox="0 0 30 60"><polyline points="24,10 6,30 24,50" fill="none" stroke="#555" stroke-width="2.5"/></svg>
  <svg class="slider-arrow abs arrow-right" viewBox="0 0 30 60"><polyline points="6,10 24,30 6,50" fill="none" stroke="#555" stroke-width="2.5"/></svg>
  <div class="portrait abs" role="img" aria-label="Portrait photo of the customer giving the testimonial"></div>
  <span class="quote-mark abs">“</span>
  <span class="testimonial-rule abs"></span>
  <p class="testimonial-text abs">Morbi diam mauris viverra in gravida eu mattis in ante Morbi eget orcu Morbi porta libero id ullamcorper nonummy nibh ligula pulvinar metus eget consectetuer augue nisi quis</p>
  <p class="testimonial-author abs">BY AUTHOR NAME</p>
  <div class="dots abs"><span></span><span></span><span></span><span></span><span></span></div>
</section>

<footer class="site-footer">
  <a class="brand footer-brand abs" href="#"><span class="brand-dot"></span>TallowVPN</a>
  <div class="footer-col abs" style="left:392px">
    <h4>COMPANY</h4>
    <ul><li>Home</li><li>About Us</li><li>Why Us</li><li>Pricing</li><li>VPN Apps</li></ul>
  </div>
  <div class="footer-col abs" style="left:545px">
    <h4>SERVICES</h4>
    <ul><li>Curabitur vel mi</li><li>Sit amet magna malesu</li><li>Aftrices Ut nisi erat</li><li>Fermentum vel</li><li>Congue id euismod</li></ul>
  </div>
  <div class="footer-col abs" style="left:736px">
    <h4>RESOURCES</h4>
    <ul><li>Support</li><li>FAQ</li><li>Help</li><li>Career</li><li>Contact Us</li></ul>
  </div>
  <div class="footer-col abs" style="left:891px">
    <h4>SUBLINKS</h4>
    <ul><li>Dis non nunc</li><li>Nulla rhoncus dictum</li><li>Aetus Curabitur</li><li>Tristique</li></ul>
  </div>
  <div class="footer-bottom abs"></div>
  <p class="copyright abs">© 2018 Company Name. All right reserved</p>
  <div class="social abs"><span></span><span></span><span></span><span></span></div>
</footer>

</body>
</html>
```